Garage Flooring Flyer

We are looking for a flyer design for our garage flooring company. We specialise in installing garage floor coatings. We use industrial grade products and are serious about durability and quality.
We target male car enthusiasts and want to project the image of a modern high-tech company. The flyer should be stunningly visual and incorporate the logo and photos we have attached. Other photos or images are welcomed.
Some key mentions to be made on the flyer are listed below:
About Us
"We are K*** R***** LLC, Home of the garage enthusiasts and Waukesha’s premier garage floor installer"
Services
Garage Floor Coatings
Offers
-Call or Email for a FREE estimate!
Credentials
-QN logo
-Pictavo Logo
-Zorbin Logo
-5stars?
Benefit Highlights to be mentioned or listed (not in any particular order)
-Industrial Quality and Strength
-Easy to Clean
-Many Color Options
-Locally Owned and Operated
-Satisfaction Guaranteed
-Lifetime Limited Warranty
-Increases Home Value
-MAKE YOUR FRIENDS AND NEIGHBORS JEALOUS!
-Fully Insured
-Certified and Trusted Installer
-Oil and Chemical Resistant
-UV Stable
-Impact and Abrasion Resistant
Contact Info
-Phone
-Email
-Website
Captions
-"From diamond grinding surface prep to using only the highest industrial-grade products, we believe in taking the time to ensure a proper installation and guarantee a durable long-lasting and beautiful garage floor";
-Serving Southeastern Wisconsin!

```html
<!DOCTYPE html>
<html lang="en">
<head>
<meta charset="utf-8">
<title>Garage Flooring Flyer</title>
<link rel="stylesheet" href="https://fonts.googleapis.com/css2?family=Oswald:wght@500;600;700&family=Fira+Sans:ital,wght@0,400;0,600;1,600&family=Open+Sans:wght@300;400&display=swap">
<style>
  :root {
    --ink: #141414;
    --ink-soft: #222324;
    --cyan: #00b0d8;
    --cyan-light: #7fd6ec;
    --silver: #c9cbcd;
    --grey-band: #6d6e70;
    --orange: #f7a941;
    --bullet: #f26a2b;
    --white: #ffffff;
    --gold: #f5c51c;
  }
  * { margin: 0; padding: 0; box-sizing: border-box; }
  html, body { width: 1166px; height: 1200px; overflow: hidden; background: #e9e9e9; }
  .stage { position: relative; width: 1166px; height: 1200px; }
  .flyer {
    position: absolute; left: 116px; top: 0;
    width: 943px; height: 1212px;
    transform: scale(0.9901); transform-origin: top left;
    background: radial-gradient(ellipse at 30% 70%, var(--ink-soft), var(--ink) 70%);
    overflow: hidden;
    font-family: 'Open Sans', sans-serif; color: var(--white);
  }
  .layer { position: absolute; left: 0; top: 0; width: 943px; height: 1212px; }
  .logo { position: absolute; left: 44px; top: 52px; width: 320px; color: var(--cyan-light); text-align: center; }
  .logo-mark { font-family: 'Oswald', sans-serif; font-weight: 700; font-size: 86px; line-height: 96px; letter-spacing: 0.04em; }
  .logo-word { font-family: 'Fira Sans', sans-serif; font-weight: 600; font-size: 30px; letter-spacing: 0.55em; margin-top: 6px; padding-left: 0.55em; }
  .tagline { position: absolute; left: 43px; top: 212px; font-family: 'Fira Sans', sans-serif; font-weight: 600; font-size: 17px; line-height: 24px; }
  .headline { position: absolute; right: 58px; top: 44px; font-family: 'Oswald', sans-serif; font-weight: 700; text-align: right; line-height: 1; }
  .headline-top { font-size: 96px; letter-spacing: 0.09em; margin-right: -0.09em; }
  .headline-bottom { font-size: 96px; letter-spacing: 0; margin-top: -10px; }
  .about { position: absolute; right: 44px; top: 282px; text-align: right; font-family: 'Fira Sans', sans-serif; font-weight: 600; font-size: 28px; line-height: 40.5px; }
  .socials { position: absolute; right: 44px; top: 634px; display: flex; gap: 10px; }
  .social { display: flex; align-items: center; gap: 5px; font-family: 'Fira Sans', sans-serif; font-weight: 600; font-size: 15px; color: var(--white); height: 44px; }
  .social::before { content: ""; width: 12px; height: 12px; background: var(--white); }
  .stars { position: absolute; right: 44px; top: 700px; }
  .website { position: absolute; left: 43px; top: 732px; font-family: 'Oswald', sans-serif; font-weight: 600; font-size: 37px; line-height: 46px; }
  .benefits { position: absolute; left: 43px; top: 806px; list-style: none; font-weight: 300; font-size: 16px; line-height: 24.85px; }
  .benefits li { padding-left: 24px; position: relative; }
  .benefits li::before { content: ""; position: absolute; left: 0; top: 7px; width: 12px; height: 12px; border-radius: 50%; background: var(--bullet); }
  .divider { position: absolute; left: 466px; top: 810px; width: 2px; height: 306px; background: #8a8a8a; }
  .quote { position: absolute; left: 503px; top: 807px; width: 396px; font-family: 'Fira Sans', sans-serif; font-style: italic; font-weight: 600; font-size: 14.6px; line-height: 22.6px; }
  .offer { position: absolute; left: 503px; top: 926px; font-family: 'Oswald', sans-serif; font-weight: 600; font-size: 38px; line-height: 45px; color: var(--orange); }
  .phone { position: absolute; left: 502px; top: 1026px; font-family: 'Oswald', sans-serif; font-weight: 700; font-size: 52px; line-height: 64px; }
  .email { position: absolute; left: 503px; top: 1097px; font-weight: 400; font-size: 22px; line-height: 30px; }
  .region { position: absolute; left: 43px; top: 1160px; font-family: 'Fira Sans', sans-serif; font-size: 25px; line-height: 34px; }
  .warranty { position: absolute; left: 503px; top: 1159px; font-family: 'Fira Sans', sans-serif; font-size: 28px; line-height: 34px; letter-spacing: 0.01em; }
</style>
</head>
<body>
<div class="stage">
  <div class="flyer">
    <svg class="layer" viewBox="0 0 943 1212" aria-hidden="true">
      <defs>
        <linearGradient id="silver" x1="0" x2="1">
          <stop offset="0" stop-color="#8d8f91"/><stop offset=".5" stop-color="#f2f3f4"/><stop offset="1" stop-color="#8d8f91"/>
        </linearGradient>
      </defs>
      <polygon points="361,0 384,0 714,770 690,770" fill="var(--cyan-light)"/>
      <polygon points="384,0 943,0 943,770 714,770" fill="var(--cyan)"/>
      <rect x="0" y="287" width="486" height="6" fill="url(#silver)"/>
      <rect x="0" y="1146" width="943" height="6" fill="url(#silver)"/>
      <polygon points="0,1152 480,1152 457,1212 0,1212" fill="var(--cyan)"/>
      <polygon points="480,1152 943,1152 943,1212 457,1212" fill="var(--grey-band)"/>
    </svg>

    <svg class="layer" viewBox="0 0 943 1212" role="img" aria-label="Photo of a finished garage with a speckled grey epoxy floor, a white sports car raised on a four-post lift and a metal-panelled ceiling">
      <defs>
        <linearGradient id="photo" x1="0" y1="0" x2="0" y2="1">
          <stop offset="0" stop-color="#cfd3d6"/><stop offset=".45" stop-color="#9ea3a7"/><stop offset="1" stop-color="#e4e5e6"/>
        </linearGradient>
      </defs>
      <polygon points="0,293 486,293 684,752 0,752" fill="url(#photo)"/>
    </svg>

    <svg class="layer" viewBox="0 0 943 1212" aria-hidden="true">
      <polygon points="0,722 419,722 455,784 0,784" fill="var(--cyan)"/>
      <polygon points="435,752 700,752 688,770 452,770" fill="#2a2b2c"/>
    </svg>

    <div class="logo">
      <div class="logo-mark">K***</div>
      <div class="logo-word">R*****</div>
    </div>
    <p class="tagline">We use industrial grade products and are<br>serious about durability and quality.</p>

    <h1 class="headline">
      <div class="headline-top">GARAGE</div>
      <div class="headline-bottom">FLOORING</div>
    </h1>

    <p class="about">We are K*** R*****<br>LLC, Home of the<br>garage enthusiasts<br>and Waukesha’s<br>premier garage<br>floor installer</p>

    <div class="socials">
      <span class="social">QN</span>
      <span class="social">Pictavo</span>
      <span class="social">Zorbin</span>
    </div>
    <svg class="stars" width="152" height="30" viewBox="0 0 152 30" role="img" aria-label="Five star rating">
      <defs>
        <polygon id="star" points="15,1 18.5,10.5 28.5,10.8 20.6,17 23.4,27 15,21.2 6.6,27 9.4,17 1.5,10.8 11.5,10.5" fill="var(--gold)" stroke="#a37a10" stroke-width="1"/>
      </defs>
      <use href="#star" x="0"/><use href="#star" x="30.5"/><use href="#star" x="61"/><use href="#star" x="91.5"/><use href="#star" x="122"/>
    </svg>

    <p class="website">www.KRFloors.com</p>

    <ul class="benefits">
      <li>Industrial Quality and Strength</li>
      <li>Easy to Clean</li>
      <li>Oil and Chemical Resistant</li>
      <li>Many Color Options</li>
      <li>Locally Owned and Operated</li>
      <li>Fully Insured</li>
      <li>Lifetime Limited Warranty</li>
      <li>Satisfaction Guaranteed</li>
      <li>Increases Home Value</li>
      <li>MAKE YOUR FRIENDS AND NEIGHBORS JEALOUS!</li>
      <li>Certified and Trusted Installer</li>
      <li>UV Stable</li>
      <li>Impact and Abrasion Resistant</li>
    </ul>

    <div class="divider"></div>

    <p class="quote">"From diamond grinding surface prep to using only the highest industrial-grade products, we believe in taking<br>the time to ensure a proper installation and guarantee a<br>durable long-lasting and beautiful garage floor"</p>

    <p class="offer">OFFERS &amp; FREE ESTIMATE<br>Call or Email</p>
    <p class="phone">555-014-2273</p>
    <p class="email">info@KRFloors.com</p>

    <p class="region">Serving Southeastern Wisconsin!</p>
    <p class="warranty">LIFETIME LIMITED WARRANTY</p>
  </div>
</div>
</body>
</html>
```